New website design

Hello again, we need you to create a basic, standard website with a homepage, 'contact us' page with reply form, 'pricing page' and 'about us' page. We would like to see most design elements carried over from www.pilvarotek.com, our primary website. You can also use the front page of the attached brochure as inspiration for the homepage. The second attachment shows the pricing page (image on the right) with vertical columns - that's a good template for you to use on the pricing page for the website. The third attachment contains the text for the pricing page...just don't use that layout, try and duplicate the vertical layout example.
Target Market(s)
hospitals/medical care facilities
Coding
Coded - Design and coding required
Number of Pages Required
4 page

```html
<!DOCTYPE html>
<html lang="en">
<head>
<meta charset="utf-8">
<title>Pilvarotek Medical – Quality Assembly and Packaging</title>
<link href="https://fonts.googleapis.com/css2?family=Montserrat:wght@400;500;600;700;800&family=Open+Sans:wght@400;600;700&display=swap" rel="stylesheet">
<style>
:root{
  --blue:#135f9c;
  --blue-dark:#0b4676;
  --navy:#0c1c2e;
  --ink:#1c2430;
  --muted:#5f6b78;
  --light:#eef3f7;
  --line:#d9e2ea;
  --white:#ffffff;
}
*{box-sizing:border-box;margin:0;padding:0}
html,body{width:1200px;height:4132px;overflow:hidden}
body{font-family:"Open Sans",sans-serif;color:var(--ink);background:var(--white);position:relative}
h1,h2,h3,h4,.brand,.btn,.nav a{font-family:"Montserrat",sans-serif}
.btn{display:inline-block;background:var(--blue);color:var(--white);font-size:12px;font-weight:700;letter-spacing:.5px;padding:12px 26px;border-radius:24px;text-transform:uppercase}

/* header */
.site-header{position:absolute;top:0;left:0;width:1200px;height:80px;background:var(--white);display:flex;align-items:center;padding:0 60px;z-index:5;box-shadow:0 2px 8px rgba(0,0,0,.08)}
.brand{display:flex;flex-direction:column;line-height:1}
.brand-name{font-size:30px;font-weight:700;color:var(--blue)}
.brand-sub{font-size:8px;letter-spacing:1.4px;color:var(--muted);margin-top:4px;text-transform:uppercase}
.nav{margin-left:auto;display:flex;gap:34px;align-items:center}
.nav a{font-size:12px;font-weight:600;color:var(--ink);text-decoration:none;text-transform:uppercase}
.nav a.active{color:var(--blue)}
.nav .phone{background:var(--blue);color:var(--white);padding:10px 20px;border-radius:22px;font-weight:700}

/* hero */
.hero{position:absolute;top:80px;left:0;width:1200px;height:800px;overflow:hidden}
.hero-photo{position:absolute;inset:0;background:linear-gradient(100deg,#0a2238 0%,#1d4669 40%,#5e7f98 70%,#b9c6d0 100%)}
.hero-content{position:absolute;left:60px;top:170px;width:680px;color:var(--white)}
.hero h1{font-size:58px;font-weight:800;line-height:1.12;margin-bottom:26px}
.hero p{font-size:14px;line-height:1.6;opacity:.9;margin-bottom:30px;width:380px}
.hero-curve{position:absolute;left:0;bottom:0;width:1200px;height:160px}

/* features */
.features{position:absolute;top:860px;left:0;width:1200px;height:180px;display:flex;padding:0 110px;gap:70px}
.feature{flex:1}
.feature svg{width:38px;height:38px;margin-bottom:10px}
.feature h3{font-size:18px;font-weight:700;margin-bottom:10px}
.feature p{font-size:13px;line-height:1.6;color:var(--muted)}

/* about */
.about{position:absolute;top:1040px;left:0;width:1200px;height:420px;padding:40px 0 0 160px}
.about-text{width:520px}
.section-title{font-size:34px;font-weight:800;letter-spacing:1px;text-transform:uppercase;margin-bottom:8px}
.title-bar{width:60px;height:4px;background:var(--blue);margin-bottom:24px}
.about p{font-size:13px;line-height:1.7;color:var(--muted);margin-bottom:16px}
.about-photo{position:absolute;left:740px;top:50px;width:330px;height:330px;border-radius:50%;border:10px solid var(--blue);background:radial-gradient(circle at 40% 40%,#e8eef3,#9eb3c4 70%,#5b7790);box-shadow:0 0 0 6px var(--light)}

/* tagline */
.tagline{position:absolute;top:1460px;left:0;width:1200px;height:320px;background:linear-gradient(180deg,#f6f8fa,#e3e9ee)}
.tagline h2{position:absolute;top:110px;left:0;width:1200px;text-align:center;font-size:30px;font-weight:800;line-height:1.35;color:var(--ink)}

/* services */
.services{position:absolute;top:1720px;left:0;width:1200px;height:700px}
.services-bg{position:absolute;inset:0;width:1200px;height:700px}
.services h2{position:absolute;top:150px;left:0;width:1200px;text-align:center;color:var(--white);font-size:34px;font-weight:800;letter-spacing:1px}
.services .title-bar{position:absolute;top:200px;left:570px;background:var(--white)}
.service-card{position:absolute;top:240px;left:250px;width:700px;height:400px;background:var(--white);border-radius:14px;box-shadow:0 12px 30px rgba(0,0,0,.2);overflow:hidden}
.tabs{display:flex;border-bottom:1px solid var(--line)}
.tab{flex:1;text-align:center;padding:18px 10px;font-family:"Montserrat",sans-serif;font-size:13px;font-weight:600;line-height:1.3}
.tab.active{background:var(--white);border-bottom:3px solid var(--blue);color:var(--blue)}
.tab:not(.active){background:var(--light)}
.service-body{display:flex;padding:36px;gap:30px}
.service-body .copy{flex:1}
.service-body p{font-size:12.5px;line-height:1.65;color:var(--muted);margin-bottom:14px}
.service-photo{width:280px;height:230px;border-radius:10px;background:linear-gradient(135deg,#dfe7ee,#8ea7bc 60%,#3f6384)}

/* pricing */
.pricing{position:absolute;top:2420px;left:0;width:1200px;height:640px}
.pricing h2{text-align:center;font-size:34px;font-weight:800;padding-top:110px}
.pricing .title-bar{margin:10px auto 40px}
.price-grid{display:flex;justify-content:center;gap:36px}
.price-card{position:relative;width:320px;background:var(--white);border-radius:10px;box-shadow:0 8px 24px rgba(16,50,80,.14);overflow:hidden;text-align:center}
.price-head{background:var(--light);padding:30px 20px 22px}
.price-card.featured .price-head{background:var(--blue);color:var(--white)}
.price-label{font-size:10px;letter-spacing:1.5px;text-transform:uppercase;opacity:.75}
.price-kind{font-family:"Montserrat",sans-serif;font-size:22px;font-weight:800;margin:6px 0}
.price-amt{font-family:"Montserrat",sans-serif;font-size:30px;font-weight:800}
.price-amt small{font-size:11px;font-weight:600}
.ribbon{position:absolute;top:14px;right:-34px;width:130px;transform:rotate(45deg);background:var(--blue-dark);color:var(--white);font-size:10px;font-weight:700;letter-spacing:1px;padding:5px 0}
.price-body{padding:22px 26px 28px}
.price-body h4{font-size:14px;font-weight:700;line-height:1.4;margin-bottom:12px}
.price-body p{font-size:12px;line-height:1.6;color:var(--muted);margin-bottom:20px}
.wave-divider{position:absolute;top:3040px;left:0;width:1200px;height:120px}

/* solutions */
.solutions{position:absolute;top:3160px;left:0;width:1200px;height:620px}
.solutions h2{text-align:center;font-size:34px;font-weight:800;padding-top:20px}
.solutions .title-bar{margin:10px auto 40px}
.solution-grid{display:flex;justify-content:center;gap:90px}
.solution{width:300px;text-align:center}
.solution-photo{width:240px;height:240px;margin:0 auto 24px;border-radius:50%;border:8px solid var(--light);box-shadow:0 0 0 3px var(--blue)}
.solution h3{font-size:16px;font-weight:700;margin-bottom:10px}
.solution p{font-size:12.5px;line-height:1.6;color:var(--muted)}

/* footer */
.site-footer{position:absolute;top:3780px;left:0;width:1200px;height:352px;background:linear-gradient(180deg,#0c1c2e,#0a1522);color:#c9d3dc}
.footer-main{display:flex;padding:70px 60px 0 60px;gap:60px;height:300px}
.footer-brand .brand-name{color:var(--white);font-size:28px}
.footer-brand .brand-sub{color:#9fb0c0}
.social{display:flex;margin-top:30px}
.social span{width:34px;height:34px;border-radius:50%;background:var(--white);display:inline-block}
.footer-col h4{color:var(--white);font-size:15px;font-weight:700;margin-bottom:16px}
.footer-col ul{list-style:none}
.footer-col li{font-size:12px;line-height:2.1;display:flex;align-items:center;gap:8px}
.footer-col li svg{width:13px;height:13px;flex:none}
.col-sitemap{margin-left:110px;width:160px}
.col-contact{width:260px}
.col-services{width:200px}
.copyright{height:52px;border-top:1px solid rgba(255,255,255,.1);text-align:center;font-size:11px;line-height:52px;color:#8a9aab}
</style>
</head>
<body>

<header class="site-header">
  <div class="brand">
    <span class="brand-name">Pilvarotek</span>
    <span class="brand-sub">Medical Packaging &amp; Sterilization</span>
  </div>
  <nav class="nav">
    <a class="active">Home</a>
    <a>Services</a>
    <a>About Us</a>
    <a>Pricing</a>
    <a>Support</a>
    <a class="phone">(555) 614-9072</a>
  </nav>
</header>

<section class="hero">
  <div class="hero-photo" role="img" aria-label="Gloved hands sealing sterile medical packaging in a cleanroom"></div>
  <div class="hero-content">
    <h1>Quality Assembly<br>and Packaging</h1>
    <p>Pilvarotek Medical is certified to requirements of ISO 13485:2016 for contract packaging and sterilization of medical products.</p>
    <span class="btn">Contact Us</span>
  </div>
  <svg class="hero-curve" viewBox="0 0 1200 160" preserveAspectRatio="none">
    <path d="M0 60 Q600 200 1200 40 L1200 160 L0 160 Z" fill="#ffffff"/>
  </svg>
</section>

<section class="features">
  <div class="feature">
    <svg viewBox="0 0 24 24"><path d="M12 2a7 7 0 0 0-7 7c0 5 7 13 7 13s7-8 7-13a7 7 0 0 0-7-7zm0 9.5A2.5 2.5 0 1 1 12 6.5a2.5 2.5 0 0 1 0 5z" fill="#135f9c"/></svg>
    <h3>Our Location</h3>
    <p>Pilvarotek Medical is located in the beautiful Central Coast of California, half-way between two major cities.</p>
  </div>
  <div class="feature">
    <svg viewBox="0 0 24 24"><path d="M3 21V8l6-3v4l6-3v4l6-3v14z" fill="#135f9c"/><rect x="6" y="14" width="3" height="4" fill="#fff"/><rect x="11" y="14" width="3" height="4" fill="#fff"/><rect x="16" y="14" width="3" height="4" fill="#fff"/></svg>
    <h3>Our Facility</h3>
    <p>Our modern 30,000 square foot facility was designed to exceed industry requirements and client needs.</p>
  </div>
  <div class="feature">
    <svg viewBox="0 0 24 24"><circle cx="12" cy="12" r="4" fill="none" stroke="#135f9c" stroke-width="3"/><path d="M12 1v4M12 19v4M1 12h4M19 12h4M4.2 4.2l2.8 2.8M17 17l2.8 2.8M4.2 19.8L7 17M17 7l2.8-2.8" stroke="#135f9c" stroke-width="3"/></svg>
    <h3>Our Expertise</h3>
    <p>Pilvarotek Medical has a wide range of expertise in contract manufacturing and packaging processes.</p>
  </div>
</section>

<section class="about">
  <div class="about-text">
    <h2 class="section-title">About Us</h2>
    <div class="title-bar"></div>
    <p>Pilvarotek Medical, Inc. offers efficient and fully compliant assembly, packaging and in-house sterilization services to the medical device industry, with contract capabilities and a team that understands demanding clinical needs.</p>
    <p>Sterilization runs are customized to product-specific requirements. The company is dedicated to industrial sterilization requirements and meets the highest industry standards in accordance with ISO 13485 and certified cleanroom classifications.</p>
    <span class="btn">Meet Our Team</span>
  </div>
  <div class="about-photo" role="img" aria-label="Technician working at a packaging station in the facility"></div>
</section>

<section class="tagline">
  <h2>Allow us to help you navigate every regulatory<br>hurdle that comes with bringing your product<br>to market</h2>
</section>

<section class="services">
  <svg class="services-bg" viewBox="0 0 1200 700" preserveAspectRatio="none">
    <path d="M0 90 Q300 0 600 60 T1200 40 L1200 700 L0 700 Z" fill="#135f9c"/>
  </svg>
  <h2>OUR SERVICES</h2>
  <div class="title-bar"></div>
  <div class="service-card">
    <div class="tabs">
      <div class="tab active">Sterilization</div>
      <div class="tab">Packaging</div>
      <div class="tab">Contract<br>Manufacturing</div>
      <div class="tab">New Product<br>Introduction</div>
    </div>
    <div class="service-body">
      <div class="copy">
        <p>As FDA accepted form of sterilization compliant with ISO 11135:2014 standards, we provide low temperature ethylene oxide sterilization and battery friendly processes for your complex devices.</p>
        <p>Uses high-energy electrons to penetrate and sterilize packaging and sensitive products quickly and effectively.</p>
        <span class="btn">Contact Us</span>
      </div>
      <div class="service-photo" role="img" aria-label="Gloved hand loading trays into a sterilization chamber"></div>
    </div>
  </div>
</section>

<section class="pricing">
  <h2>PRICING LIST</h2>
  <div class="title-bar"></div>
  <div class="price-grid">
    <div class="price-card">
      <div class="ribbon">NEW</div>
      <div class="price-head">
        <div class="price-label">Standard</div>
        <div class="price-kind">ON SITE</div>
        <div class="price-amt">$195 <small>/HOUR</small></div>
      </div>
      <div class="price-body">
        <h4>Emergency Priority service Technicians Typically On-Premises Within 24 Hours</h4>
        <p>Electronic device failure is one of the few certainties in life; we don't know when trusted critical devices will malfunction if well prepared and safe.</p>
        <span class="btn">Book Now</span>
      </div>
    </div>
    <div class="price-card featured">
      <div class="ribbon">NEW</div>
      <div class="price-head">
        <div class="price-label">Limited Regional</div>
        <div class="price-kind">ON SITE</div>
        <div class="price-amt">$225 <small>/HOUR</small></div>
      </div>
      <div class="price-body">
        <h4>Emergency Priority service Technicians Typically On-Premises Within 24 Hours</h4>
        <p>Electronic device failure is one of the few certainties in life; we don't know when trusted critical devices will malfunction if well prepared and safe.</p>
        <span class="btn">Book Now</span>
      </div>
    </div>
    <div class="price-card">
      <div class="ribbon">NEW</div>
      <div class="price-head">
        <div class="price-label">Limited Regional</div>
        <div class="price-kind">OFF SITE</div>
        <div class="price-amt">$175 <small>/HOUR</small></div>
      </div>
      <div class="price-body">
        <h4>Emergency Priority service Technicians Typically On-Premises Within 24 Hours</h4>
        <p>Electronic device failure is one of the few certainties in life; we don't know when trusted critical devices will malfunction if well prepared and safe.</p>
        <span class="btn">Book Now</span>
      </div>
    </div>
  </div>
</section>

<svg class="wave-divider" viewBox="0 0 1200 120" preserveAspectRatio="none">
  <path d="M0 70 Q300 0 600 50 T1200 30 L1200 70 Q900 120 600 80 T0 100 Z" fill="#135f9c"/>
  <path d="M0 100 Q300 70 600 80 T1200 70 L1200 85 Q900 120 600 100 T0 115 Z" fill="#0b4676"/>
</svg>

<section class="solutions">
  <h2>PRICING LIST</h2>
  <div class="title-bar"></div>
  <div class="solution-grid">
    <div class="solution">
      <div class="solution-photo" role="img" aria-label="Gloved hands handling sterile vials" style="background:linear-gradient(135deg,#cfdde8,#5d88ad)"></div>
      <h3>Sterilization Solutions</h3>
      <p>ISO Class 7 (Class 10,000) state-of-the-art cleanrooms maintain the standards that provide the highest standard of sterile environment for your procedures.</p>
    </div>
    <div class="solution">
      <div class="solution-photo" role="img" aria-label="Automated assembly and packaging line" style="background:linear-gradient(135deg,#dde5ec,#7d97ad)"></div>
      <h3>Quality Assembly and Packaging</h3>
      <p>Pilvarotek Medical is certified to requirements of the ISO 13485:2016 for contract packaging and sterilization of medical products.</p>
    </div>
    <div class="solution">
      <div class="solution-photo" role="img" aria-label="Technician in protective suit inside a cleanroom" style="background:linear-gradient(135deg,#e4eef5,#8fb4cf)"></div>
      <h3>Cleanrooms</h3>
      <p>ISO Class 7 (Class 10,000) state-of-the-art cleanrooms maintain the standards that provide the highest standard of sterile environment for your products.</p>
    </div>
  </div>
</section>

<footer class="site-footer">
  <div class="footer-main">
    <div class="footer-brand">
      <div class="brand">
        <span class="brand-name">Pilvarotek</span>
        <span class="brand-sub">Medical Packaging &amp; Sterilization</span>
      </div>
      <div class="social"><span></span></div>
    </div>
    <div class="footer-col col-sitemap">
      <h4>Site Map</h4>
      <ul><li>Home</li><li>About Us</li><li>Services</li><li>Support</li><li>Careers</li><li>Contact Us</li></ul>
    </div>
    <div class="footer-col col-contact">
      <h4>Contact Us</h4>
      <ul>
        <li><svg viewBox="0 0 24 24"><path d="M12 2a7 7 0 0 0-7 7c0 5 7 13 7 13s7-8 7-13a7 7 0 0 0-7-7z" fill="#4f9ad6"/></svg>418 Harlow Row, Marendale, CA 90000</li>
        <li><svg viewBox="0 0 24 24"><rect x="2" y="5" width="20" height="14" rx="2" fill="#4f9ad6"/><path d="M2 6l10 7 10-7" stroke="#0c1c2e" stroke-width="2" fill="none"/></svg>info@pilvarotek.com</li>
        <li><svg viewBox="0 0 24 24"><path d="M6 2l4 5-2 3a12 12 0 0 0 6 6l3-2 5 4-3 4C10 22 2 14 2 5z" fill="#4f9ad6"/></svg>(555) 614-9072</li>
        <li><svg viewBox="0 0 24 24"><rect x="3" y="7" width="18" height="12" rx="2" fill="#4f9ad6"/></svg>(555) 614-9073</li>
        <li><svg viewBox="0 0 24 24"><circle cx="12" cy="12" r="9" fill="none" stroke="#4f9ad6" stroke-width="2.5"/></svg>www.pilvarotek.com</li>
      </ul>
    </div>
    <div class="footer-col col-services">
      <h4>Services</h4>
      <ul><li>Sterilization</li><li>Packaging</li><li>Contract Manufacturing</li><li>New Product Introduction</li><li>Cleanrooms</li></ul>
    </div>
  </div>
  <div class="copyright">© 2024 Pilvarotek Medical - All Right Reserved</div>
</footer>

</body>
</html>
```